Accountant website

Please design a accountant website for www.fenwaylodgeadvisory.com.au. This site is majorly out of date, and is not supported by modern browsers.

The style should use the reds from the design at dev.fenwaylodgeadvisory.com.au, and should be modern and make use of Slides (large content slides that the user scrolls through on the front page).

The content is largely already on the site, however happy to move some around to suit the modern design as required.

The dev.fenwaylodgeadvisory.com.au was a rough mock up that I have completed that the client is "happy" with the direction, however this needs a lot of polish and finishing touches, and I will accept designs that differ from this, but highly recommend that this is used as a guide.

Ready to be sliced PSD Only - HTML no required.

In all honesty, although I can technically do a lot of this, the polished finished I want for this site has eluded me in a few attempts, and therefore I am looking out there at you much more artistic people to finish (or redesign if required) this site.

Target Market(s)

Higher end Small - Medium Business

Industry/Entity Type

Accountant

Requirements
Must have
• Must use the logo from dev.fenwaylodgeadvisory.com.au use exactly the red colours as defined in this layout. A basic layout PSD (to get the colour etc) and the logo in ai format is attached to this project. Please ignore the SSL warning on the development site.

The final product does NOT have to be the same as shown on dev.fenwaylodgeadvisory.com.au however the red colour scheme must be used. The client DOES want the logo on the RIGHT.

Must have a front landing page design, and a page layout that considers the other page content (at least one separate PSD)
Nice to have
• I really am looking at a slide format for the front page simular to:

http://www.plumvine.com/au/
http://www.tidelockbox.com/

The attached photos should be used on the site. Was considering a rotating banner with these images are a watermark background on a solid Red header bar, but happy to be shown other options.
Should not have
• Please no "Pattern Goblin" submissions.

```html
<!DOCTYPE html>
<html lang="en">
<head>
<meta charset="utf-8">
<title>Fenway Lodge Advisory</title>
<link href="https://fonts.googleapis.com/css2?family=Cabin:wght@400;500;600;700&family=Arimo:wght@400;700&display=swap" rel="stylesheet">
<style>
:root{
  --red:#c4161c;
  --red-bright:#e3262b;
  --ink:#222;
  --text:#555;
  --grey-icon:#8e979c;
  --band:#f4f4f4;
  --footer:#2e2e2e;
  --footer-base:#242424;
  --rule:#e6e6e6;
}
*{margin:0;padding:0;box-sizing:border-box}
html,body{width:780px;height:1200px;overflow:hidden;background:#fff}
body{position:relative;font-family:"Arimo",Arial,sans-serif;color:var(--text)}
.abs{position:absolute}

/* header */
.site-header{left:0;top:0;width:780px;height:84px;background:#fff}
.brand{right:67px;top:22px;display:flex;align-items:center;gap:8px}
.brand-square{width:12px;height:12px;background:var(--red)}
.brand-name{font-family:"Cabin",sans-serif;font-weight:700;color:var(--ink);font-size:21px;line-height:20px;letter-spacing:.3px;text-align:right}
.brand-name small{display:block;font-size:10.5px;line-height:13px;letter-spacing:.2px;font-weight:700}
.login-box{left:66px;top:10px;width:248px;height:61px;background:#f5f5f5;border:1px solid #e4e4e4;border-radius:3px}
.login-field{position:absolute;top:9px;width:107px;height:16px;background:#fff;border:1px solid #e1e1e1;font-family:"Cabin",sans-serif;font-size:7.5px;color:#999;padding:3px 5px}
.login-links{position:absolute;left:67px;top:32px;font-family:"Cabin",sans-serif;font-size:8px;line-height:11px;color:#333}
.login-links u{color:#333}
.login-btn{position:absolute;left:178px;top:33px;width:54px;height:19px;background:var(--red);border-radius:3px;color:#fff;font-family:"Cabin",sans-serif;font-size:11.5px;text-align:center;line-height:19px}

/* hero */
.hero{left:0;top:84px;width:780px;height:293px;background:linear-gradient(180deg,#b9c7d2 0%,#8fa2b1 18%,#4f6f92 32%,#3d5f86 60%,#4a5a6c 85%,#6a5e52 100%)}
.hero-caption{left:66px;top:138px;width:330px;height:146px;background:rgba(40,44,50,.82);border-radius:3px;padding:11px 10px}
.hero-caption h1{font-family:"Cabin",sans-serif;font-weight:500;font-size:20.5px;color:#fff;line-height:24px}
.hero-caption h1 span{color:var(--red-bright)}
.hero-caption p{font-family:"Cabin",sans-serif;font-size:8.8px;line-height:14.4px;color:#fff;margin-top:6px;width:302px}
.dots{position:absolute;left:11px;top:118px;display:flex;gap:5px}
.dots i{width:12px;height:12px;border-radius:50%;background:#ddd;border:2px solid #bbb}
.dots i.on{background:#444;border-color:#ddd}

/* features */
.feature-title{font-family:"Cabin",sans-serif;font-weight:500;color:var(--red);font-size:19.5px}
.feature-text{font-size:10px;line-height:14.4px;color:var(--text)}
.divider{left:66px;top:562px;width:647px;height:1px;background:var(--rule)}

/* team */
.team{left:0;top:795px;width:780px;height:253px;background:var(--band)}
.member{position:absolute;width:200px;text-align:center}
.member-photo{width:156px;height:156px;border-radius:50%;margin:0 auto;border:3px solid #fff;box-shadow:0 0 0 1px #ddd}
.member-name{font-weight:700;color:var(--red);font-size:10.5px;letter-spacing:.3px;margin-top:20px}
.member-role{font-size:10.5px;color:#444;margin-top:1px}

/* footer */
.site-footer{left:0;top:1048px;width:780px;height:128px;background:var(--footer)}
.footer-col{position:absolute;top:13px}
.footer-col h4{font-family:"Cabin",sans-serif;font-weight:700;font-size:8.5px;color:#fff;letter-spacing:-.1px}
.footer-col p{font-family:"Cabin",sans-serif;font-size:8.5px;line-height:13.6px;color:#eee}
.post-date{font-family:"Cabin",sans-serif;font-size:7px;color:#999;margin-top:14px}
.footer-brand{position:absolute;left:72px;top:88px;font-family:"Cabin",sans-serif;font-weight:700;color:#fff;font-size:17px;line-height:16px}
.footer-brand small{display:block;font-size:8px;line-height:10px}
.tags{display:flex;flex-wrap:wrap;gap:4px 3px;width:140px;margin-top:16px}
.tags span{border:1px solid #555;font-family:"Cabin",sans-serif;font-size:7px;color:#ddd;padding:5px 6px;line-height:8px}
.thumbs{display:grid;grid-template-columns:repeat(4,31px);gap:5px;margin-top:16px}
.thumbs div{width:31px;height:31px;border:2px solid #555}
.footer-base{left:0;top:1176px;width:780px;height:24px;background:var(--footer-base);text-align:center;font-size:8px;line-height:24px;color:#888}
</style>
</head>
<body>

<header class="abs site-header">
  <div class="abs login-box">
    <div class="login-field" style="left:12px">Username</div>
    <div class="login-field" style="left:128px">Password</div>
    <div class="login-links">Forgot login?<br>No account yet? <u>Register</u></div>
    <div class="login-btn">Login</div>
  </div>
  <div class="abs brand">
    <div class="brand-square"></div>
    <div class="brand-name">FENWAY LODGE<small>ADVISORY</small></div>
  </div>
</header>

<section class="abs hero" role="img" aria-label="Photo of a smiling consultant in a red dress seated on a harbour jetty with water and city buildings behind"></section>
<div class="abs hero-caption">
  <h1>When First <span>Impressions Count...</span></h1>
  <p>I attended a local solicitors' office this morning and upon arriving was immediately impressed with the appearance of the reception and waiting area. The receptionist greeted me warmly and instructed ...<br>Full story</p>
  <div class="dots"><i class="on"></i><i></i><i></i><i></i></div>
</div>

<svg class="abs" style="left:66px;top:407px" width="290" height="118" viewBox="0 0 290 118" aria-hidden="true">
  <rect x="25" y="0" width="170" height="104" rx="4" fill="var(--grey-icon)"/>
  <rect x="32" y="7" width="156" height="90" fill="#fff"/>
  <circle cx="110" cy="3.5" r="1.2" fill="#fff"/>
  <path d="M0 106h217v4a3 3 0 0 1-3 3H3a3 3 0 0 1-3-3z" fill="var(--grey-icon)"/>
  <rect x="90" y="106" width="36" height="3" rx="1.5" fill="#d6dadc"/>
  <g fill="var(--red-bright)">
    <path d="M207 75h10v-3l5 5-5 5v-3h-10z"/>
    <path d="M221 81h-10v3l-5-5 5-5v3h10z" transform="translate(0 5)"/>
  </g>
  <rect x="249" y="49" width="32" height="68" rx="4" fill="#4a4f52"/>
  <rect x="253" y="57" width="24" height="46" fill="#fff"/>
  <circle cx="265" cy="110" r="3" fill="#fff"/>
</svg>
<h2 class="abs feature-title" style="left:373px;top:416px">Getting to Fenway Lodge Advisory</h2>
<p class="abs feature-text" style="left:373px;top:455px;width:340px">Fenway Lodge Advisory aims to service the needs of its clients by focusing on the present rather than reporting on historical figures. We recognise that business owners benefit from regular contact with their accountant. One who undertakes a hands on approach in working with business owners to improve their business.</p>

<div class="abs divider"></div>

<h2 class="abs feature-title" style="left:70px;top:606px">Fenway Lodge Advisory Difference</h2>
<p class="abs feature-text" style="left:70px;top:641px;width:355px">Not all Accountants are created equally … the Fenway Lodge Advisory difference Fenway Lodge Advisory takes pride in not following the status quo, the following points are just some of the unique benefits you will experience when working with us.<br><br>Believing in the here and now: A proactive accountant that focuses on providing timely and relevant information.</p>
<svg class="abs" style="left:444px;top:622px" width="265" height="104" viewBox="0 0 265 104" aria-hidden="true">
  <path d="M22 100a22 22 0 0 1-4-43 28 28 0 0 1 38-24A40 40 0 0 1 127 38a33 33 0 0 1 7 62z" fill="var(--grey-icon)"/>
  <path d="M67 101V72H52l23-28 23 28H83v29z" fill="#fff"/>
  <path d="M172 72l-9 12h6l-6 10 12-13h-6l6-9z" fill="var(--red-bright)"/>
  <circle cx="236" cy="79" r="19" fill="none" stroke="#3f4447" stroke-width="5"/>
  <path d="M236 68v12h8" fill="none" stroke="#3f4447" stroke-width="3.5" stroke-linecap="round"/>
  <path d="M213 65a10 10 0 0 1 12-12z M259 65a10 10 0 0 0-12-12z" fill="#3f4447"/>
  <path d="M223 96l-5 6M249 96l5 6" stroke="#3f4447" stroke-width="3.5" stroke-linecap="round"/>
</svg>

<section class="abs team">
  <div class="member" style="left:52px;top:38px">
    <div class="member-photo" role="img" aria-label="Portrait of Daniel Hewitt at a marina" style="background:radial-gradient(circle at 50% 45%,#c9a68a 0%,#6b4a36 55%,#8496a6 100%)"></div>
    <div class="member-name">Daniel Hewitt</div>
    <div class="member-role">UX Designer/Partner</div>
  </div>
  <div class="member" style="left:291px;top:36px">
    <div class="member-photo" role="img" aria-label="Portrait of Fenway team partner in a red top at a marina" style="background:radial-gradient(circle at 50% 40%,#d7a184 0%,#b2472e 45%,#b8213a 70%,#8fa1ae 100%)"></div>
    <div class="member-name">Fenway</div>
    <div class="member-role">UX Designer/Partner</div>
  </div>
  <div class="member" style="left:535px;top:40px">
    <div class="member-photo" role="img" aria-label="Portrait of Marion Keller at a marina" style="background:radial-gradient(circle at 50% 40%,#d4ab8e 0%,#7a5438 50%,#3a3a3e 80%,#8fa1ae 100%)"></div>
    <div class="member-name">Marion Keller</div>
    <div class="member-role">UX Designer/Partner</div>
  </div>
</section>

<footer class="abs site-footer">
  <div class="footer-col" style="left:71px;width:146px">
    <h4>SUPPORT</h4>
    <p style="margin-top:14px">For assistance or questions for our products, make sure you visit our support forums or call us at</p>
  </div>
  <div class="footer-brand">FENWAY LODGE<small>ADVISORY</small></div>
  <div class="footer-col" style="left:242px;width:150px">
    <h4>DIARY POSTS</h4>
    <div class="post-date">APRIL 6TH, 2013</div>
    <p>It's time to tell our story right from the beginning</p>
    <div class="post-date" style="margin-top:8px">MARCH 27TH, 2013</div>
    <p>Take away the sorrow from my heart</p>
  </div>
  <div class="footer-col" style="left:413px">
    <h4>DIARY TAGS</h4>
    <div class="tags">
      <span>DREAMY</span><span>ETERNITY</span><span>MUSIC</span>
      <span>OTHER STORIES</span><span>POETRY</span>
      <span>UNIVERSE</span><span>WALL</span>
    </div>
  </div>
  <div class="footer-col" style="left:572px">
    <h4>PHOTO STREAM</h4>
    <div class="thumbs">
      <div role="img" aria-label="Photo stream thumbnail" style="background:#9cc0a8"></div>
      <div role="img" aria-label="Photo stream thumbnail" style="background:#d0502a"></div>
      <div role="img" aria-label="Photo stream thumbnail" style="background:#e6d4c0"></div>
      <div role="img" aria-label="Photo stream thumbnail" style="background:#4f79c4"></div>
      <div role="img" aria-label="Photo stream thumbnail" style="background:#4a4d7a"></div>
      <div role="img" aria-label="Photo stream thumbnail" style="background:#bfe2c4"></div>
      <div role="img" aria-label="Photo stream thumbnail" style="background:#3e5fa8"></div>
      <div role="img" aria-label="Photo stream thumbnail" style="background:#e8ecd8"></div>
    </div>
  </div>
</footer>
<div class="abs footer-base">2013 © Fenway Lodge. ALL Rights Reserved. Privacy Policy | Terms of Service</div>

</body>
</html>
```